Business Card

To design a professional business card for myself a Beauty Therapist. I will be selling Sol Varenne tanning and other products from home (a beauty room). I have uploaded a file of there promo and I really love their colours. I'm looking for a classey feel to the design, simple but effective. I require my name Tessa Marlowe Beauty Therapist, Mobile- 0413952817, Email - tessa.marlowe@qelmail.com, Facebook - /tessamarlowebeauty & instagram - tessamarlowebeautytherapist . I would like the logo for facebook and instagram. I will also need a A5 & A4 flyer. text futura book to be used.

```html
<!DOCTYPE html>
<html lang="en">
<head>
<meta charset="utf-8">
<title>Tessa Marlowe Beauty Therapist – Business Card</title>
<link rel="stylesheet" href="https://fonts.googleapis.com/css2?family=Abel&display=swap">
<style>
  :root {
    --turquoise: #5cd0c7;
    --water-light: #8fe6ea;
    --water-mid: #5fd6dc;
    --water-deep: #3fc4cc;
    --paper: #ffffff;
    --frame: #000000;
    --card-font: "Abel", "Futura", sans-serif;
  }
  * { margin: 0; padding: 0; box-sizing: border-box; }
  html, body {
    width: 1200px;
    height: 752px;
    overflow: hidden;
    background: var(--paper);
  }
  .sheet {
    position: relative;
    width: 1200px;
    height: 752px;
    background: var(--paper);
    font-family: var(--card-font);
  }
  .card {
    position: absolute;
    left: 0;
    width: 582px;
    height: 358px;
    border: 5px solid var(--frame);
    background: var(--paper);
    overflow: hidden;
  }
  .card--front { top: 0; }
  .card--back { top: 391px; }

  .water {
    position: absolute;
    left: 0; top: 0;
    width: 100%;
    height: 238px;
    background:
      radial-gradient(ellipse at 20% 30%, rgba(255,255,255,0.35), transparent 45%),
      radial-gradient(ellipse at 75% 60%, rgba(255,255,255,0.25), transparent 50%),
      linear-gradient(160deg, var(--water-light), var(--water-mid) 50%, var(--water-deep));
  }
  .rule {
    position: absolute;
    left: 127px;
    width: 315px;
    height: 5px;
    background: var(--turquoise);
  }
  .rule--white { background: var(--paper); }

  .front-name {
    position: absolute;
    left: 0; width: 100%;
    top: 142px;
    text-align: center;
    color: var(--paper);
    font-size: 82px;
    line-height: 1;
    letter-spacing: -1px;
    text-transform: uppercase;
    transform: scaleX(0.86);
    white-space: nowrap;
  }
  .front-title {
    position: absolute;
    left: 0; width: 100%;
    top: 254px;
    text-align: center;
    color: var(--turquoise);
    font-size: 32px;
    line-height: 1;
    text-transform: uppercase;
    transform: scaleX(0.82);
    white-space: nowrap;
  }

  .contact-line {
    position: absolute;
    left: 0; width: 100%;
    text-align: center;
    color: var(--turquoise);
    font-size: 27px;
    line-height: 1;
    white-space: nowrap;
  }
  .social {
    position: absolute;
    left: 129px;
    display: flex;
    align-items: center;
    gap: 16px;
    color: var(--turquoise);
    font-size: 27px;
    line-height: 1;
    white-space: nowrap;
  }
  .social__mark {
    width: 28px;
    height: 28px;
    background: var(--turquoise);
    flex: none;
  }
</style>
</head>
<body>
<main class="sheet">

  <section class="card card--front" aria-label="Business card front">
    <div class="water" role="img" aria-label="Rippling turquoise pool water"></div>
    <div class="rule rule--white" style="top:130px"></div>
    <h1 class="front-name">Tessa Marlowe</h1>
    <p class="front-title">Beauty Therapist</p>
    <div class="rule" style="top:304px"></div>
  </section>

  <section class="card card--back" aria-label="Business card back">
    <div class="rule" style="top:54px"></div>
    <p class="contact-line" style="top:76px">Tessa Marlowe Beauty Therapist</p>
    <p class="contact-line" style="top:120px">Mobile - 0413952817</p>
    <p class="contact-line" style="top:165px">Email - tessa.marlowe@qelmail.com</p>
    <p class="social" style="top:213px"><span class="social__mark" aria-hidden="true"></span>/tessamarlowebeauty</p>
    <p class="social" style="top:258px"><span class="social__mark" aria-hidden="true"></span>tessamarlowebeautytherapist</p>
    <div class="rule" style="top:308px"></div>
  </section>

</main>
</body>
</html>
```